Brochure Redesign

We need a new, adapted, design for our Brochure. A few weeks ago we've setup a new Homepage design and for now we want to adapt our old Brochure to the new design.

Requirements:
-) Place the 3 products quite prominent
-) Place also our add ons
-) Use the Keyvisuals you can find on the Homepage

New Homepage: www.rufkontor.at
Old Folder version - see attached

Requirements
Must have
• Logo and basic design from Homepage

```html
<!DOCTYPE html>
<html lang="de">
<head>
<meta charset="utf-8">
<title>Rufkontor Folder</title>
<link href="https://fonts.googleapis.com/css2?family=Arimo:wght@400;700&display=swap" rel="stylesheet">
<style>
:root{
  --wine:#7b1519;
  --orange:#f39200;
  --yellow:#fcd836;
  --gold:#f7b500;
  --grey:#e6e6e6;
  --text:#4a4a4a;
  --white:#ffffff;
}
*{margin:0;padding:0;box-sizing:border-box}
html,body{width:1200px;height:961px;overflow:hidden;background:var(--white)}
body{position:relative;font-family:"Arimo",Arial,sans-serif;color:var(--text)}
.abs{position:absolute}
.crop{position:absolute;background:#999}

/* left panel */
.hero-left{left:95px;top:124px;width:337px;height:320px}
.benefits-title{left:131px;top:154px;color:var(--white);font-weight:700;font-size:17px;line-height:20px}
.benefits{left:131px;top:198px;list-style:none;font-size:11.5px;color:var(--white)}
.benefits li{height:21.6px;display:flex;align-items:center;gap:8px}
.benefits li.highlight{color:var(--yellow);font-weight:700}
.tick{width:14px;height:14px;flex:none}

.step{left:126px;width:278px}
.step-bar{position:absolute;left:0;top:0;bottom:0;width:30px;background:var(--wine);border-radius:18px 0 0 18px;color:var(--white);font-weight:700;font-size:28px;display:flex;align-items:flex-end;justify-content:center;padding-bottom:6px}
.step-body{position:absolute;left:30px;right:0;top:18px;bottom:0;background:var(--grey);padding:8px 10px 6px 46px;font-size:9.5px;line-height:12px;color:#555}
.step-tag{position:absolute;right:0;top:0;width:140px;height:20px;background:linear-gradient(90deg,#fff3b0,var(--gold));color:var(--wine);font-weight:700;font-size:11px;display:flex;align-items:center;justify-content:flex-end;padding-right:12px}
.step-photo{position:absolute;left:-4px;top:-24px;width:66px;height:66px;border-radius:50%;border:3px solid var(--white);box-shadow:0 1px 3px rgba(0,0,0,.3)}

/* middle panel */
.hero-mid{left:432px;top:124px;width:336px;height:400px}
.bubble{left:477px;top:144px;width:172px;height:140px}
.bubble-text{left:506px;top:186px;width:122px;color:var(--wine)}
.bubble-text h3{font-size:13px;font-weight:700}
.bubble-text p{font-size:8.5px;line-height:10px;margin-top:3px}
.app-visual{left:658px;top:222px;width:74px;height:120px;border-radius:10px;background:linear-gradient(160deg,#555,#222 40%,#e9a23b 60%,#8a1a1a)}
.store-badge{left:482px;top:294px;width:98px;height:34px;border-radius:5px;background:#111;border:1px solid #777}
.store-badge-alt{left:594px;top:288px;width:40px;height:42px;border-radius:8px;background:#9bbf3a}
.advantages{left:474px;top:370px;color:var(--wine)}
.advantages h2{font-size:26px;font-weight:700}
.advantages h4{font-size:15px;font-weight:700;margin-top:2px}
.advantages ul{list-style:none;font-size:10.5px;line-height:13px;margin-top:3px}
.trial{left:472px;top:545px;width:252px}
.trial h2{color:var(--wine);font-size:17px;font-weight:700;margin-bottom:10px}
.trial p{font-size:10px;line-height:12.4px}
.trial b{color:var(--wine)}
.costs{left:472px;top:690px;width:240px;font-size:9.5px}
.costs h3{background:#e0e0e0;color:var(--wine);font-size:12px;font-weight:700;height:19px;padding-left:8px;line-height:19px}
.costs table{width:100%;border-collapse:collapse;margin-top:10px}
.costs td{padding:0 0 0 8px;line-height:11.5px}
.costs td.amount{width:52px;padding:0}
.costs tr.total td{padding-top:12px}

/* right panel */
.addons-head{left:768px;top:124px;width:336px;height:48px;background:var(--wine);color:var(--white);font-weight:700;font-size:18px;display:flex;align-items:center;justify-content:center}
.addon-icon{width:76px;height:76px;border-radius:50%;background:radial-gradient(circle at 40% 35%,#fff38a,var(--gold) 70%);border:2px solid #fff6c0;box-shadow:0 1px 4px rgba(0,0,0,.25)}
.addon-icon span{display:block;margin:18px auto;width:38px;height:38px;border-radius:6px}
.price{background:var(--yellow);color:var(--wine);font-weight:700;font-size:14px;border-radius:3px;height:24px;display:flex;align-items:center;justify-content:center}
.addon-title{color:var(--wine);font-weight:700;font-size:14px;width:336px;left:768px;text-align:center}
.addon-text{left:812px;width:248px;font-size:9px;line-height:11px;text-align:justify;color:#555}
.mini-price{top:718px;width:66px;height:38px;background:var(--yellow);border-radius:3px;color:var(--wine);text-align:center;font-weight:700}
.mini-price small{display:block;font-size:6.5px;line-height:7px;padding-top:4px}
.mini-price strong{font-size:14px}
</style>
</head>
<body>

<!-- crop marks -->
<div class="crop" style="left:70px;top:124px;width:16px;height:1px"></div>
<div class="crop" style="left:95px;top:98px;width:1px;height:16px"></div>
<div class="crop" style="left:432px;top:98px;width:1px;height:16px"></div>
<div class="crop" style="left:768px;top:98px;width:1px;height:16px"></div>
<div class="crop" style="left:1104px;top:98px;width:1px;height:16px"></div>
<div class="crop" style="left:1114px;top:124px;width:16px;height:1px"></div>
<div class="crop" style="left:70px;top:836px;width:16px;height:1px"></div>
<div class="crop" style="left:95px;top:846px;width:1px;height:16px"></div>
<div class="crop" style="left:432px;top:846px;width:1px;height:16px"></div>
<div class="crop" style="left:768px;top:846px;width:1px;height:16px"></div>
<div class="crop" style="left:1104px;top:846px;width:1px;height:16px"></div>
<div class="crop" style="left:1114px;top:836px;width:16px;height:1px"></div>

<!-- LEFT PANEL -->
<svg class="abs hero-left" viewBox="0 0 337 320">
  <path d="M0 262C100 320 270 305 337 232V262C270 335 100 335 0 290Z" fill="var(--orange)"/>
  <path d="M0 0H337V232C270 305 100 320 0 262Z" fill="var(--wine)"/>
</svg>
<h1 class="abs benefits-title">DAS BIETET IHNEN<br>RUFKONTOR.AT</h1>
<ul class="abs benefits">
  <li><svg class="tick" viewBox="0 0 14 14"><circle cx="7" cy="7" r="7" fill="var(--gold)"/><path d="M3.5 7.2l2.3 2.3 4.6-4.8" stroke="#fff" stroke-width="1.8" fill="none"/></svg>Ihr Unternehmen ist 24h / 365 Tage erreichbar</li>
  <li><svg class="tick" viewBox="0 0 14 14"><circle cx="7" cy="7" r="7" fill="var(--gold)"/><path d="M3.5 7.2l2.3 2.3 4.6-4.8" stroke="#fff" stroke-width="1.8" fill="none"/></svg>Alle Daten online abruf- und änderbar</li>
  <li><svg class="tick" viewBox="0 0 14 14"><circle cx="7" cy="7" r="7" fill="var(--gold)"/><path d="M3.5 7.2l2.3 2.3 4.6-4.8" stroke="#fff" stroke-width="1.8" fill="none"/></svg>Persönliche Anrufentgegennahme</li>
  <li><svg class="tick" viewBox="0 0 14 14"><circle cx="7" cy="7" r="7" fill="var(--gold)"/><path d="M3.5 7.2l2.3 2.3 4.6-4.8" stroke="#fff" stroke-width="1.8" fill="none"/></svg>Individueller Meldetext</li>
  <li><svg class="tick" viewBox="0 0 14 14"><circle cx="7" cy="7" r="7" fill="var(--gold)"/><path d="M3.5 7.2l2.3 2.3 4.6-4.8" stroke="#fff" stroke-width="1.8" fill="none"/></svg>Gesprächsnotizen jederzeit online abrufbar</li>
  <li><svg class="tick" viewBox="0 0 14 14"><circle cx="7" cy="7" r="7" fill="var(--gold)"/><path d="M3.5 7.2l2.3 2.3 4.6-4.8" stroke="#fff" stroke-width="1.8" fill="none"/></svg>Im ersten Monat keine Grundgebühr</li>
  <li class="highlight"><svg class="tick" viewBox="0 0 14 14"><circle cx="7" cy="7" r="7" fill="var(--gold)"/><path d="M3.5 7.2l2.3 2.3 4.6-4.8" stroke="#fff" stroke-width="1.8" fill="none"/></svg>Keine Kündigungsfrist</li>
  <li class="highlight"><svg class="tick" viewBox="0 0 14 14"><circle cx="7" cy="7" r="7" fill="var(--gold)"/><path d="M3.5 7.2l2.3 2.3 4.6-4.8" stroke="#fff" stroke-width="1.8" fill="none"/></svg>Keine Einrichtungskosten</li>
  <li class="highlight"><svg class="tick" viewBox="0 0 14 14"><circle cx="7" cy="7" r="7" fill="var(--gold)"/><path d="M3.5 7.2l2.3 2.3 4.6-4.8" stroke="#fff" stroke-width="1.8" fill="none"/></svg>Keine Mindestvertragslaufzeit</li>
</ul>

<section class="abs step" style="top:462px;height:86px">
  <div class="step-bar">1</div>
  <div class="step-body" style="text-align:center">Das Service-Paket "Rund um die Uhr" steht Ihnen 24 Stunden am Tag, 365 Tage im Jahr zur Verfügung. Die Servicezeiten umfassen damit auch Sonn- und Feiertage.</div>
  <div class="step-tag">Dateneingabe</div>
  <div class="step-photo" role="img" aria-label="Photo: hands typing on a keyboard" style="background:linear-gradient(135deg,#f5e6d8,#c9b29a)"></div>
</section>

<section class="abs step" style="top:594px;height:86px">
  <div class="step-bar">2</div>
  <div class="step-body">Sofort nach erfolgreicher Buchung erhalten Sie Ihre Zielrufnummer. Leiten Sie Ihr Telefon einfach auf diese Nummer um (Hilfe).</div>
  <div class="step-tag">Rufumleitung</div>
  <div class="step-photo" role="img" aria-label="Photo: hand holding a mobile phone" style="background:linear-gradient(135deg,#e8d6c8,#6b6b6b)"></div>
</section>

<section class="abs step" style="top:732px;height:88px">
  <div class="step-bar">3</div>
  <div class="step-body">Ihr neues Sekretariat ist nun aktiv. Sie und all Ihre Mitarbeiter werden in Echtzeit, individuell über eingehende Anrufe informiert.</div>
  <div class="step-tag">Ihr Sekretariat</div>
  <div class="step-photo" role="img" aria-label="Photo: call center agent with headset" style="background:linear-gradient(135deg,#f1dcc2,#c79a6a)"></div>
</section>

<!-- MIDDLE PANEL -->
<svg class="abs hero-mid" viewBox="0 0 336 400">
  <defs>
    <linearGradient id="warm" x1="0" y1="0" x2="0" y2="1">
      <stop offset="0" stop-color="var(--orange)"/>
      <stop offset="0.55" stop-color="var(--yellow)"/>
      <stop offset="1" stop-color="var(--gold)"/>
    </linearGradient>
  </defs>
  <path d="M0 120Q60 20 200 40Q280 48 336 20V400H0Z" fill="url(#warm)"/>
  <path d="M0 368Q150 400 336 384V400H0Z" fill="var(--white)"/>
</svg>
<svg class="abs bubble" viewBox="0 0 172 112" preserveAspectRatio="none">
  <path d="M8 6Q80 -4 150 12Q170 18 166 40L160 80Q158 92 146 92H120L140 112 96 92H18Q6 92 6 80L2 20Q2 8 8 6Z" fill="var(--wine)"/>
  <path d="M14 14Q80 6 146 20Q158 24 156 40L152 76Q150 84 142 84H22Q12 84 12 74L10 24Q10 16 14 14Z" fill="var(--yellow)"/>
</svg>
<div class="abs bubble-text">
  <h3>Kostenlose App</h3>
  <p>Laden Sie jetzt die kostenlose Rufkontor App direkt online herunter.</p>
</div>
<div class="abs app-visual" role="img" aria-label="Illustration: smartphone showing the app"></div>
<div class="abs store-badge"></div>
<div class="abs store-badge-alt"></div>

<div class="abs advantages">
  <h2>Ihre Vorteile</h2>
  <h4>Einfach, Immer, Erreichbar</h4>
  <ul>
    <li>- Individueller Meldetext</li>
    <li>- Beliebig viele Mitarbeiter</li>
    <li>- 24h Erreichbarkeit</li>
    <li>- Ohne Mindestvertragslaufzeit</li>
    <li>- Keine versteckten Callminuten</li>
  </ul>
</div>

<div class="abs trial">
  <h2>24h - GRATIS -TEST</h2>
  <p><b>Jederzeit unverbindlich einen Tag kostenlos auf rufkontor.at testen.</b> Einfach Meldetext sowie Firmen- und Personendaten eingeben, schon wird der Testzugang vollautomatisch eingerichtet. Sobald Sie sich von den Vorteilen Ihres neuen Sekretariats überzeugt haben, können Sie innerhalb der 24-stündigen Testphase gleich online buchen, indem Sie Ihre Zahlungsdaten ergänzen.</p>
</div>

<div class="abs costs">
  <h3>KOSTEN</h3>
  <table>
    <tr><td>Monatl. Grundgebühr</td><td class="amount"></td></tr>
    <tr><td>Service-Paket "Bürozeiten"</td><td class="amount">€ 29,00</td></tr>
    <tr><td>50 Anrufe pro Monat</td><td class="amount">€ 99,50</td></tr>
    <tr><td>11 Sofortbenachrichtigungen per SMS</td><td class="amount">€ 3,30</td></tr>
    <tr><td>Telefonspesen</td><td class="amount">€ 4,70</td></tr>
    <tr class="total"><td>Gesamtaufwand</td><td class="amount">€ 136,50</td></tr>
  </table>
</div>

<!-- RIGHT PANEL -->
<div class="abs addons-head">ADD ON'S</div>

<div class="abs addon-icon" style="left:898px;top:198px"><span role="img" aria-label="Icon: safe with magnifying glass" style="background:#d9833a"></span></div>
<div class="abs price" style="left:912px;top:278px;width:50px">€ 19,-</div>
<div class="abs addon-title" style="top:308px">Online Wissensdatenbank</div>
<p class="abs addon-text" style="top:326px">Our online knowledge base forms the basis for the professional storage of your information and serves as an interface between your experts, call center and customer. Structured information processing allows searches by keyword, category and / or free text.</p>

<div class="abs addon-icon" style="left:898px;top:410px"><span role="img" aria-label="Icon: calendar" style="background:#e8e2d8"></span></div>
<div class="abs price" style="left:912px;top:489px;width:50px">€ 29,-</div>
<div class="abs addon-title" style="top:520px">Online Terminkalender</div>
<p class="abs addon-text" style="top:538px">Sämtliche Anforderungen wie Terminlängen, Kategorien, Zeitfenster,etc. werden individuell an Ihre Bedürfnisse angepasst und ermöglichen ortsunabhängig alle Termine zu verwalten. Eine Tages- oder Wochenansicht bietet zusätzlich einen strukturierten Gesamtüberblick aller Termine.</p>

<div class="abs addon-icon" style="left:898px;top:640px"><span role="img" aria-label="Icon: studio microphone" style="background:#9a9a9a;width:24px;border-radius:12px"></span></div>
<div class="abs mini-price" style="left:817px"><small>Neutrale<br>Bandansage</small><strong>€ 4,90</strong></div>
<div class="abs mini-price" style="left:893px"><small>Personalisierte<br>Bandansage</small><strong>€ 7,90</strong></div>
<div class="abs mini-price" style="left:969px;width:82px"><small>Anrufbeantworterfunktion<br>&nbsp;</small><strong>€ 9,90</strong></div>
<div class="abs addon-title" style="top:762px">Tonbänder &amp; Co</div>
<p class="abs addon-text" style="top:781px;text-align:center">Sie haben die Möglichkeit mit neutralen und individuellen Bandansagen oder einer Anrufbeantworterfunktion Ihren Kunden noch mehr Service zu bieten.</p>

</body>
</html>
```